Corporate consulting business needs a business card

I want a professional business card.... surprise me

Updates

Reason: i dont think 2 days is enough

Target Market(s)

Corprorate and Not for Profit firms and organisations

Industry/Entity Type

Consulting

Contact Information for Business Card

Logo
Corporate Consulting Services
On Time, On Budget, Beyond Expectation
Tovan Presfield
Director
0427 31 94 62 (Larger)
tovan@tp-advisory.com.au
www.tp-advisory.com.au
include little icons beside the contact info:

- Envelope = email
- Phone = phone
- Globe = website

Font styles to use
Serif
Sans Serif

Requirements
Must have
• Professional and clean
Nice to have
• you tell me

```html
<!DOCTYPE html>
<html lang="en">
<head>
<meta charset="utf-8">
<title>TP Advisory – Business Card</title>
<link rel="stylesheet" href="https://fonts.googleapis.com/css2?family=Tinos:wght@400;700&family=Open+Sans:wght@400&display=swap">
<style>
  :root {
    --stage: #e9e6e2;
    --card: #ffffff;
    --brown: #4e2d14;
    --ink: #1a1a1a;
    --text: #2b2b2b;
    --ghost: #ececec;
    --muted: #555555;
  }
  * { margin: 0; padding: 0; box-sizing: border-box; }
  html, body { width: 1200px; height: 471px; overflow: hidden; background: var(--stage); }
  .stage { position: relative; width: 1200px; height: 471px; }
  .card {
    position: absolute; top: 80px; width: 540px; height: 310px;
    background: var(--card); overflow: hidden;
    box-shadow: 0 6px 18px rgba(0,0,0,.18);
  }
  .card--front { left: 40px; }
  .card--back { left: 620px; }
  .card__art { position: absolute; inset: 0; }

  .holder { position: absolute; right: 28px; top: 18px; text-align: right; color: #fff; font-family: "Tinos", serif; }
  .holder__name { font-size: 22px; }
  .holder__title { font-size: 16px; margin-top: 2px; }

  .brand { position: absolute; left: 30px; top: 162px; font-family: "Tinos", serif; font-weight: 700; font-size: 22px; letter-spacing: .5px; color: var(--ink); }

  .contacts { position: absolute; left: 34px; top: 222px; list-style: none; font-family: "Tinos", serif; color: var(--text); }
  .contacts li { display: flex; align-items: center; gap: 10px; font-size: 17px; height: 26px; }
  .contacts li.contacts__phone { font-size: 18px; }
  .contacts svg { width: 12px; height: 12px; flex: none; }

  .tagline { position: absolute; left: 40px; top: 44px; font-family: "Open Sans", sans-serif; color: var(--ink); }
  .tagline__title { font-size: 19px; font-weight: 400; }
  .tagline__list { list-style: none; margin-top: 14px; }
  .tagline__list li { font-size: 14px; line-height: 22px; position: relative; padding-left: 16px; }
  .tagline__list li::before { content: ""; position: absolute; left: 2px; top: 9px; width: 6px; height: 6px; border-radius: 50%; background: var(--ink); }
  .web { position: absolute; left: 56px; bottom: 34px; font-family: "Open Sans", sans-serif; font-size: 14px; color: var(--muted); }
  .web strong { font-weight: 400; color: var(--ink); }
</style>
</head>
<body>
<main class="stage">
  <section class="card card--front">
    <svg class="card__art" viewBox="0 0 540 310" aria-hidden="true">
      <circle cx="430" cy="215" r="112" fill="none" stroke="var(--ghost)" stroke-width="5"/>
      <path d="M0,0 H540 V235 C522,120 330,10 0,14 Z" fill="var(--brown)"/>
      <path d="M0,20 C330,18 524,128 540,252 L540,272 C512,142 330,30 0,26 Z" fill="var(--ink)"/>
      <circle cx="108" cy="100" r="50" fill="none" stroke="var(--brown)" stroke-width="4"/>
    </svg>
    <div class="holder">
      <p class="holder__name">Tovan Presfield</p>
      <p class="holder__title">Director</p>
    </div>
    <p class="brand">TP ADVISORY</p>
    <ul class="contacts">
      <li class="contacts__phone">
        <svg viewBox="0 0 12 12"><rect x="3" y="0.5" width="6" height="11" rx="1" fill="var(--brown)"/><rect x="4" y="2" width="4" height="5" fill="#fff"/></svg>
        0427 31 94 62
      </li>
      <li>
        <svg viewBox="0 0 12 12"><rect x="0.5" y="2.5" width="11" height="8" fill="var(--brown)"/><path d="M1,3 L6,7 L11,3" fill="none" stroke="#fff" stroke-width="1"/></svg>
        tovan@tp-advisory.com.au
      </li>
      <li>
        <svg viewBox="0 0 12 12"><circle cx="6" cy="6" r="5.2" fill="none" stroke="var(--muted)" stroke-width="1.2"/><ellipse cx="6" cy="6" rx="2.2" ry="5.2" fill="none" stroke="var(--muted)" stroke-width="1"/><line x1="0.8" y1="6" x2="11.2" y2="6" stroke="var(--muted)" stroke-width="1"/></svg>
        www.tp-advisory.com.au
      </li>
    </ul>
  </section>

  <section class="card card--back">
    <svg class="card__art" viewBox="0 0 540 310" aria-hidden="true">
      <circle cx="455" cy="150" r="92" fill="none" stroke="var(--ghost)" stroke-width="5"/>
    </svg>
    <div class="tagline">
      <h1 class="tagline__title">Corporate Consulting Services</h1>
      <ul class="tagline__list">
        <li>On Time</li>
        <li>On Budget</li>
        <li>Beyond Expectation</li>
      </ul>
    </div>
    <p class="web">www.<strong>tp-advisory</strong>.com.au</p>
  </section>
</main>
</body>
</html>
```